Vemra. Packaging for mood-boosting energy drink mix. Upbeat and uplifting.

I need a mockup of a pouch package + a stick. I included an image of a Aqua Tarn pouch + stick for reference. I do not have a die line for the pouch, so feel free to just use the same relative dimensions for the pouch and create a rendering. Here are the specifications for the packaging that I need:
1. The logo is included in the uploaded files. Please use the one that says "bright day spark" beneath "vemra." The logo should take up about the top 1/3 to 1/2 of the pouch.
2. The pouch should be mostly white, especially behind the logo, but feel free to explore yellow or orange for the bottom 1/2 to 2/3 of the packaging.
3. In the center of the packaging, below the logo, please have the product name appear, "mood-boosting energy drink mix" similar to where "Fluid Amplifier" is placed.
4. Below that, create an image of a glass with a stick pouring into it like in the Aqua Tarn pouch.
5. Below the glass, in the bottom center of the package, include "16 sticks. Net Wt. 4 oz. (114 g)
6. On the left side, please include callouts, from top to bottom, "energy blend (80mg caffeine, taurine) + happy blend (saffron, st. john's wort, rhodiola).
7. On the right side, please include callouts, from top to bottom, "electrolytes + vitamins + 0g sugar"
8. Somewhere else on the front of the packaging, please include the flavor name "golden berry," perhaps where they do on the aqua tarn pouch.
9. For the stick, use your creativity.
10. There is no back of packaging to design for this project.

Target Market(s)

My target consumer leads a very active lifestyle and cares deeply about health & wellness.

Colors
0094D4
00A9DD
6FCCEA
C7EBF8
E9F6FB
FFC000
F8CF3A
FAE287
FDF2CF
FEFAEE
F0912C
F2A743
F7CA91
FBE8D2
FDF5EE
EE7325
F08F49
F5BC92
FAE3D3
FDF4ED

Requirements
Must have
• My packaging must make people feel good and maybe even smile when they see it. A brand that does this well is Penn. (www.pennvita-example.com)
Nice to have
• I like 60's Mod Design if you need some inspiration. The packaging should also convey a sense of levity. Like you'll float or dance through life after drinking this.

```html
<!DOCTYPE html>
<html lang="en">
<head>
<meta charset="utf-8">
<title>Vemra – Mood-Boosting Energy Drink Mix Packaging</title>
<link rel="stylesheet" href="https://fonts.googleapis.com/css2?family=Arimo:wght@400;700&family=Poppins:wght@400;500;600;700&display=swap">
<style>
  :root {
    --orange: #F08133;
    --orange-deep: #EE7325;
    --yellow: #F0B63C;
    --yellow-soft: #F6CE7A;
    --white: #FFFFFF;
    --grey-light: #E4E5E7;
    --grey-text: #DADBDD;
    --grey-mid: #8E9094;
  }
  * { margin: 0; padding: 0; box-sizing: border-box; }
  html, body { width: 1200px; height: 900px; overflow: hidden; background: var(--white); }
  .canvas { position: relative; width: 1200px; height: 900px; background: var(--white); font-family: Arimo, Arial, sans-serif; }

  /* Pouch */
  .pouch { position: absolute; left: 205px; top: 88px; width: 639px; height: 717px; border: 1px solid #F1F1F2; overflow: hidden; background: var(--white); }
  .pouch-art { position: absolute; inset: 0; }
  .pouch-tagline { position: absolute; left: 41px; top: 18px; color: var(--grey-text); font-family: Arimo, Arial, sans-serif; }
  .pouch-tagline .lead { display: block; font-weight: 700; font-size: 25px; letter-spacing: -1.5px; line-height: 1.1; }
  .pouch-tagline .sub { display: block; font-family: Poppins, sans-serif; font-weight: 500; font-size: 19px; line-height: 1.1; }
  .count-ribbon { position: absolute; left: 538px; top: 0; width: 79px; text-align: center; color: var(--white); font-family: Poppins, sans-serif; }
  .count-ribbon .num { display: block; font-weight: 600; font-size: 32px; line-height: 1; margin-top: 12px; letter-spacing: -1px; }
  .count-ribbon .label { display: block; font-weight: 500; font-size: 11.5px; line-height: 1.15; }

  .brand { position: absolute; left: 0; right: 0; top: 112px; text-align: center; }
  .brand-name { display: inline-block; font-family: Poppins, sans-serif; font-weight: 700; font-size: 118px; line-height: 1; letter-spacing: -4px; color: var(--orange-deep); }
  .brand-tag { position: absolute; left: 0; right: 0; top: 218px; text-align: center; padding-left: 130px; font-family: Poppins, sans-serif; font-weight: 500; font-size: 17px; color: var(--orange-deep); }

  .product-name { position: absolute; left: 0; right: 0; top: 305px; text-align: center; color: var(--white); font-weight: 700; }
  .product-name .main { display: block; font-size: 44px; letter-spacing: -2.5px; line-height: 1; }
  .product-name .type { display: block; font-size: 23px; letter-spacing: -1.2px; margin-top: 12px; }

  .serve-art { position: absolute; left: 130px; top: 392px; width: 332px; height: 136px; border-radius: 10px; background: linear-gradient(135deg, #F6CE7A 0%, #F3A257 100%); }

  .callout { position: absolute; color: var(--white); font-weight: 700; writing-mode: vertical-rl; white-space: nowrap; }
  .callout-left { left: 22px; top: 360px; font-size: 12.5px; line-height: 1.25; }
  .callout-right { left: 598px; top: 360px; font-size: 15px; }

  .flavor-tag { position: absolute; left: 262px; top: 585px; width: 115px; height: 25px; background: var(--white); color: var(--yellow); font-family: Arimo, Arial, sans-serif; font-weight: 700; font-size: 14px; letter-spacing: -0.8px; text-align: center; line-height: 25px; }
  .net-weight { position: absolute; left: 0; right: 0; top: 660px; text-align: center; color: var(--orange-deep); font-family: Poppins, sans-serif; font-weight: 500; font-size: 13.5px; letter-spacing: -0.4px; }

  /* Stick */
  .stick { position: absolute; left: 876px; top: 212px; width: 131px; height: 593px; border: 1px solid #F1F1F2; background: var(--white); overflow: hidden; }
  .stick-art { position: absolute; inset: 0; }
  .tear-label { position: absolute; left: 5px; top: 4px; font-size: 8.5px; color: var(--grey-mid); }
  .tear-line { position: absolute; left: 3px; right: 3px; top: 21px; border-top: 1.3px dashed #555; }
  .stick-brand { position: absolute; left: 0; right: 0; top: 90px; text-align: center; font-family: Poppins, sans-serif; font-weight: 700; font-size: 40px; letter-spacing: -1.5px; line-height: 1; color: var(--orange-deep); }
  .stick-brand-tag { position: absolute; left: 0; right: 0; top: 132px; padding-left: 50px; text-align: center; font-family: Poppins, sans-serif; font-size: 6.5px; font-weight: 500; color: var(--orange-deep); }
  .stick-name { position: absolute; left: 0; right: 0; top: 167px; text-align: center; color: var(--orange-deep); font-weight: 700; }
  .stick-name .main { display: block; font-size: 14px; letter-spacing: -0.9px; line-height: 1; }
  .stick-name .type { display: block; font-size: 7.5px; letter-spacing: -0.3px; margin-top: 3px; }
  .stick-flavor { position: absolute; left: 21px; top: 464px; width: 90px; height: 17px; background: var(--white); color: var(--yellow); font-weight: 700; font-size: 9.5px; letter-spacing: -0.5px; text-align: center; line-height: 17px; }
  .stick-note { position: absolute; left: 0; right: 0; text-align: center; color: var(--white); font-family: Poppins, sans-serif; font-weight: 500; }
  .stick-note.flavors { top: 485px; font-size: 7.5px; }
  .stick-note.water { top: 500px; font-size: 9px; }
  .stick-note.weight { top: 545px; font-size: 8.5px; }
</style>
</head>
<body>
<main class="canvas">

  <section class="pouch" aria-label="Vemra pouch front">
    <svg class="pouch-art" width="639" height="717" viewBox="0 0 639 717" aria-hidden="true">
      <g class="zip-lines" stroke="var(--grey-light)" stroke-width="2">
        <line x1="0" y1="84" x2="639" y2="84"/>
        <line x1="0" y1="89" x2="639" y2="89"/>
        <line x1="0" y1="95" x2="639" y2="95"/>
        <line x1="0" y1="100" x2="639" y2="100"/>
        <line x1="0" y1="105" x2="639" y2="105"/>
      </g>
      <path class="ribbon" d="M538 0 H617 V105 L577 84 L538 105 Z" fill="var(--orange)"/>
      <path d="M0 335 Q319.5 195 639 335 V717 H0 Z" fill="var(--yellow)"/>
      <path d="M0 346 Q319.5 212 639 346 V717 H0 Z" fill="var(--orange)"/>
      <path d="M0 617 Q319.5 533 639 617 V717 H0 Z" fill="var(--yellow)"/>
      <path d="M0 640 Q319.5 550 639 640 V717 H0 Z" fill="var(--orange)"/>
      <path d="M0 660 Q319.5 572 639 660 V717 H0 Z" fill="var(--yellow)"/>
      <path d="M0 680 Q319.5 588 639 680 V717 H0 Z" fill="var(--orange)"/>
      <path d="M0 700 Q319.5 608 639 700 V717 H0 Z" fill="var(--yellow)"/>
      <path d="M0 717 Q319.5 620 639 717 Z" fill="var(--white)"/>
    </svg>

    <p class="pouch-tagline"><span class="lead">MOOD-BOOSTING</span><span class="sub">made easy</span></p>
    <p class="count-ribbon"><span class="num">16</span><span class="label">on the go<br>packet</span></p>

    <div class="brand"><span class="brand-name">vemra</span></div>
    <p class="brand-tag">bright day spark</p>

    <h1 class="product-name"><span class="main">MOOD-BOOSTING</span><span class="type">ENERGY DRINK MIX</span></h1>

    <div class="serve-art" role="img" aria-label="Illustration of a stick pouring into a glass equal to three water drops"></div>

    <p class="callout callout-left">Energy Blend (80mg Caffeine, Taurine) +<br>Happy Blend (Saffron, St. John's Wort, Rhodiola).</p>
    <p class="callout callout-right">Electrolytes + Vitamins + 0g Sugar</p>

    <p class="flavor-tag">GOLDEN BERRY</p>
    <p class="net-weight">16 sticks. Net Wt. 4 oz. (114 g)</p>
  </section>

  <section class="stick" aria-label="Vemra single stick">
    <svg class="stick-art" width="131" height="593" viewBox="0 0 131 593" aria-hidden="true">
      <rect x="0" y="206" width="131" height="15" fill="var(--yellow)"/>
      <rect x="0" y="221" width="131" height="372" fill="var(--orange)"/>
      <rect x="0" y="515" width="131" height="15" fill="var(--yellow)"/>
      <rect x="0" y="544" width="131" height="14" fill="var(--yellow)"/>
      <rect x="0" y="578" width="131" height="15" fill="var(--yellow)"/>
    </svg>
    <p class="tear-label">Tear Across</p>
    <div class="tear-line"></div>
    <p class="stick-brand">vemra</p>
    <p class="stick-brand-tag">bright day spark</p>
    <h2 class="stick-name"><span class="main">MOOD-BOOSTING</span><span class="type">ENERGY DRINK MIX</span></h2>
    <p class="stick-flavor">GOLDEN BERRY</p>
    <p class="stick-note flavors">Natural Flavors</p>
    <p class="stick-note water">Add to 16oz water</p>
    <p class="stick-note weight">Net Wt. 4 oz. (114 g)</p>
  </section>

</main>
</body>
</html>
```